Brochure for Home Improvement Startup

We need an eye-catching, informative, and easy to read brochure design to help explain our services to our target audience which include baby boomers and seniors.

Baby

```html
<!DOCTYPE html>
<html lang="en">
<head>
<meta charset="utf-8">
<title>NestWell Solutions – Trifold Brochure</title>
<link rel="stylesheet" href="https://fonts.googleapis.com/css2?family=Lato:wght@400;700&family=Roboto:wght@700&family=Roboto+Condensed:wght@700&display=swap">
<style>
  :root {
    --pink: #e2137f;
    --pink-deep: #cf0a70;
    --pink-bright: #ee2a92;
    --ink: #1a1a1a;
    --black: #0d0d0d;
    --text: #2b2b2b;
    --paper: #ffffff;
    --grey-photo-top: #d9d9d9;
    --grey-photo-bottom: #8e8e8e;
  }
  * { margin: 0; padding: 0; box-sizing: border-box; }
  html, body {
    width: 1200px; height: 1200px; overflow: hidden;
    background: var(--paper);
    font-family: "Lato", Arial, sans-serif;
  }
  .canvas { position: relative; width: 1200px; height: 1200px; }
  .brochure {
    position: absolute; left: 79px; top: 177px;
    width: 1076px; height: 768px;
    display: flex;
    box-shadow: 0 2px 8px rgba(0,0,0,.18);
  }
  .panel { position: relative; height: 100%; overflow: hidden; background: var(--paper); }
  .panel--about { width: 358px; }
  .panel--contact {
    width: 368px;
    background: linear-gradient(90deg, #ececec 0%, #fafafa 8%, #ffffff 50%, #fafafa 92%, #ececec 100%);
  }
  .panel--cover { width: 350px; }

  .footer-band {
    position: absolute; left: 0; right: 0; bottom: 0; height: 41px;
    background: linear-gradient(90deg, var(--pink-deep), var(--pink-bright));
    color: #fff; font-size: 14px; letter-spacing: 2.6px;
    display: flex; align-items: center; justify-content: center;
  }

  /* About panel */
  .section-title {
    position: absolute; left: 29px;
    color: var(--pink); font-weight: 700; font-size: 14px; letter-spacing: .3px;
  }
  .section-text {
    position: absolute; left: 29px; width: 307px;
    color: var(--text); font-size: 12.2px; line-height: 15px; text-align: justify;
  }
  .mission-title { top: 70px; }
  .mission-text { top: 87px; }
  .focus-title { top: 150px; left: 27px; }
  .focus-text { top: 172px; }
  .about-chevron { position: absolute; left: 0; top: 290px; width: 358px; height: 110px; }
  .service-heading {
    position: absolute; left: 0; right: 0; top: 404px; text-align: center;
    font-family: "Roboto", Arial, sans-serif; font-weight: 700;
    font-size: 27px; line-height: 34px;
  }
  .service-heading .accent { color: var(--pink); display: block; }
  .service-heading .plain { color: var(--ink); display: block; }
  .about-photo {
    position: absolute; left: 0; right: 0; top: 495px; height: 227px;
    background: linear-gradient(180deg, #f5f5f5 0%, var(--grey-photo-top) 30%, var(--grey-photo-bottom) 100%);
  }

  /* Contact panel */
  .contact-art { position: absolute; left: 0; top: 0; width: 368px; height: 320px; }
  .headline {
    position: absolute; left: 0; right: 0; top: 398px; text-align: center;
    font-family: "Roboto Condensed", "Arial Narrow", sans-serif; font-weight: 700;
    color: var(--pink); font-size: 38px; line-height: 46px;
  }
  .contact-dot {
    position: absolute; left: 158px; top: 540px; width: 54px; height: 54px;
    border-radius: 50%; background: #fff; border: 2px solid var(--ink); z-index: 2;
  }
  .contact-button {
    position: absolute; left: 94px; top: 584px; width: 168px; height: 32px;
    border-radius: 16px; background: var(--pink); color: #fff;
    font-family: "Roboto", Arial, sans-serif; font-weight: 700; font-size: 15px;
    display: flex; align-items: center; justify-content: center;
  }
  .address {
    position: absolute; left: 0; right: 0; top: 630px; text-align: center;
    font-size: 12.5px; line-height: 15.5px; color: var(--ink); font-style: normal;
  }
  .phone {
    position: absolute; left: 0; right: 0; top: 682px; text-align: center;
    font-family: "Roboto Condensed", "Arial Narrow", sans-serif; font-weight: 700;
    color: var(--pink); font-size: 22px;
  }
  .contact-web {
    position: absolute; left: 0; right: 0; bottom: 14px; text-align: center;
    color: var(--ink); font-size: 14.5px; letter-spacing: 2.6px;
  }

  /* Cover panel */
  .cover-top {
    position: absolute; left: 0; top: 0; width: 350px; height: 320px;
    background: linear-gradient(180deg, #e8168a 0%, #dd3c94 55%, #d46ba6 100%);
  }
  .brand-name {
    position: absolute; left: 0; right: 0; top: 112px; text-align: center;
    color: #fff; font-weight: 700; font-size: 52px; letter-spacing: -.5px;
  }
  .cover-roof { position: absolute; left: 0; top: 200px; width: 350px; height: 120px; }
  .cover-photo {
    position: absolute; left: 0; top: 303px; width: 350px; height: 278px;
    background: linear-gradient(135deg, #c9b7a3 0%, #a9805f 40%, #8aa6c6 75%, #d6d0c7 100%);
  }
  .cover-title {
    position: absolute; left: 0; right: 0; top: 591px; height: 127px;
    background: linear-gradient(180deg, #3a3a3a 0%, var(--black) 60%, #000 100%);
    text-align: center;
    font-family: "Roboto", Arial, sans-serif; font-weight: 700;
    font-size: 38px; line-height: 42px; padding-top: 24px;
  }
  .cover-title .accent { color: var(--pink); display: block; font-family: "Roboto Condensed", "Arial Narrow", sans-serif; font-size: 42px; }
  .cover-title .plain { color: #fff; display: block; }
</style>
</head>
<body>
<div class="canvas">
  <div class="brochure">

    <section class="panel panel--about">
      <h2 class="section-title mission-title">MISSION</h2>
      <p class="section-text mission-text">maintenance of our client’s homes to enhance their overall quality of life.</p>
      <h2 class="section-title focus-title">FOCUS</h2>
      <p class="section-text focus-text">We deliver light home modification service to seniors and boomers so their homes continue to meet their changing needs. Specifically, we provide consultation and aging in place assessments to homeowners, sales, and installation of high quality grab bars, threshold ramps, lighting, and smart home technology as well ongoing home maintenance through a home “Fitness Plan”.</p>
      <svg class="about-chevron" viewBox="0 0 358 110" aria-hidden="true">
        <polygon points="0,8 179,85 358,8 358,26 179,102 0,26" fill="var(--black)"/>
      </svg>
      <h2 class="service-heading">
        <span class="accent">HOME ASSESSMENTS</span>
        <span class="plain">AND CONSULTING</span>
      </h2>
      <div class="about-photo" role="img" aria-label="Black and white photo of a large Victorian house"></div>
      <div class="footer-band">www.nestwellsolutions.com</div>
    </section>

    <section class="panel panel--contact">
      <svg class="contact-art" viewBox="0 0 368 320" aria-hidden="true">
        <defs>
          <linearGradient id="houseTone" x1="0" y1="0" x2="0" y2="1">
            <stop offset="0" stop-color="#e9ece6"/>
            <stop offset="0.6" stop-color="#a9b0a4"/>
            <stop offset="1" stop-color="#5d7a3c"/>
          </linearGradient>
        </defs>
        <rect x="0" y="0" width="368" height="308" fill="url(#houseTone)" role="img" aria-label="Photo of a two-storey house with a white wraparound porch on a green lawn"/>
        <polygon points="0,308 200,232 368,308 368,320 0,320" fill="#fff"/>
        <polygon points="200,232 368,170 368,308" fill="var(--black)"/>
      </svg>
      <h1 class="headline">MAKE YOUR HOME<br>FIT YOU!</h1>
      <div class="contact-dot" aria-hidden="true"></div>
      <div class="contact-button">CONTACT US</div>
      <address class="address">NESTWELL,<br>1480 HARBOR VIEW RD<br>TACOMA, WA 98403, USA</address>
      <p class="phone">CALL US 253.555.0184</p>
      <p class="contact-web">www.nestwellsolutions.com</p>
    </section>

    <section class="panel panel--cover">
      <div class="cover-top" role="img" aria-label="Pink-tinted photo of a house and garden"></div>
      <p class="brand-name">NestWell</p>
      <svg class="cover-roof" viewBox="0 0 350 120" aria-hidden="true">
        <polygon points="0,120 174,6 350,120 350,103 350,103 174,-8 0,103" fill="#fff"/>
        <polygon points="0,120 174,14 350,120" fill="#fff"/>
        <polyline points="0,116 174,10 350,116" fill="none" stroke="var(--black)" stroke-width="8"/>
      </svg>
      <div class="cover-photo" role="img" aria-label="Photo of a smiling senior couple standing in front of a brick house"></div>
      <h2 class="cover-title">
        <span class="accent">NESTWELL</span>
        <span class="plain">SOLUTIONS</span>
      </h2>
      <div class="footer-band">www.nestwellsolutions.com</div>
    </section>

  </div>
</div>
</body>
</html>
```